Flyer-Design
Zielgruppe
Dienstleistungen
Aufgabenstellung
Unser Folder, Din lang, 6-seitig,
soll eine neue Farbe (blau) erhalten und unser Firmenlogo muss implementiert werden.
Sonst nix. Keine weiteren Änderungen nötig/erwünscht.
Texte werden in kopierbarer Version gestellt
Der Folder wird bei Papiermondo in den Druck gegeben, deren Druckvorgaben (Beschnitt etc.) sind einzuhalten.

```html
<!DOCTYPE html>
<html lang="de">
<head>
<meta charset="utf-8">
<title>Curavita – Folder DIN lang</title>
<link rel="stylesheet" href="https://fonts.googleapis.com/css2?family=Arimo:wght@400;700&display=swap">
<style>
:root{
  --page-bg:#e9edf3;
  --blue:#2a62b6;
  --blue-dark:#1f4fa0;
  --blue-mid:#5f8fd2;
  --blue-light:#a9c3ea;
  --paper:#fbfcfe;
  --text:#2b2f38;
  --white:#ffffff;
}
*{box-sizing:border-box;margin:0;padding:0}
html,body{width:1200px;height:1037px;overflow:hidden;background:var(--page-bg);font-family:"Arimo",Arial,sans-serif;color:var(--text)}
.spread{position:absolute;left:258px;display:flex;width:684px;height:486px;box-shadow:0 4px 14px rgba(30,50,90,.18)}
.spread--outside{top:26px}
.spread--inside{top:530px}
.panel{position:relative;width:228px;height:486px;padding:22px 16px;overflow:hidden;
  background:linear-gradient(160deg,var(--paper) 0%,#e6eefa 50%,var(--blue-light) 100%);
  border-right:1px solid rgba(40,80,150,.15)}
.panel:last-child{border-right:none}
.heading{font-size:13px;font-weight:700;color:var(--blue);letter-spacing:.5px;text-transform:uppercase;padding-bottom:3px;border-bottom:1.5px solid var(--blue);margin-bottom:9px}
.subhead{font-size:6.6px;font-weight:700;margin:6px 0 3px}
.numhead{font-size:6.6px;font-weight:700;color:var(--blue);text-transform:uppercase;margin:7px 0 2px}
p{font-size:6.3px;line-height:1.38;margin-bottom:5px}
.photo{position:absolute;border-radius:50%;border:2px solid var(--blue)}
.cost-table{width:100%;border-collapse:collapse;font-size:6.2px}
.cost-table td{padding:3.5px 0;vertical-align:top}
.cost-table td:last-child{text-align:right;white-space:nowrap;padding-left:6px}
.contact{font-size:6px;line-height:1.4;width:100%;border-collapse:collapse}
.contact td{vertical-align:top;padding:2px 0}
.contact td:first-child{font-weight:700;width:44px}
.cover{background:linear-gradient(165deg,#dbe7f8 0%,var(--blue-mid) 45%,#4f80c8 100%);color:var(--white)}
.brand{font-weight:700;color:var(--white)}
.brand--cover{font-size:27px;text-align:center;margin-top:14px;line-height:1}
.tagline{font-size:8px;font-weight:700;text-align:center;margin-top:3px;color:var(--white)}
.badge{position:absolute;border-radius:50%;background:var(--blue-dark);display:flex;align-items:center;justify-content:center}
.badge .brand{font-size:11px}
.brand--inline{color:var(--blue);font-size:16px;text-align:center;margin-top:8px}
.tagline--inline{color:var(--blue);font-size:6px;text-align:center;font-weight:700}
.list-grid{display:grid;grid-template-columns:1fr 1fr;font-size:6px;gap:2px 6px;margin-bottom:4px}
</style>
</head>
<body>

<section class="spread spread--outside">
  <article class="panel">
    <h2 class="heading">Legalität</h2>
    <h3 class="subhead">Entsendung</h3>
    <p>Osteuropäische Unternehmen haben die Möglichkeit, ihre Mitarbeiter auch in Deutschland einzusetzen.</p>
    <p>Voraussetzung ist, dass die osteuropäische Firma auch über ein erhebliches Inlandsgeschäft verfügt. Auch darf der Anbieter nicht beliebig viele Mitarbeiter ins Ausland entsenden. Die Anzahl der Mitarbeiter wird in einer Quote von den zuständigen Behörden festgelegt, vereinfacht dargestellt: Je größer die Firma, desto mehr Mitarbeiter kann sie auch entsenden.</p>
    <p>Die Entsendungsdauer für einen einzelnen Mitarbeiter beträgt max. 24 Monate. Kaum ein Mitarbeiter möchte allerdings 24 Monate am Stück von zu Hause fort sein. In der Regel beträgt die Einsatzdauer daher 8 – 12 Wochen.</p>
    <p>Für jeden einzelnen Mitarbeiter, der in Deutschland tätig werden soll, muss die osteuropäische Firma eine spezielle Erlaubnis (A1) bei der zuständigen Behörde beantragen. Bis diese Erlaubnis erteilt wird, vergehen in der Regel ca. 2 – 4 Wochen; die Betreuungskraft darf aber schon vorher in Deutschland arbeiten, die Erlaubnis A1 wird dann nachgereicht.</p>
    <p>Die über Curavita vermittelten Betreuungskräfte sind bei osteuropäischen Kooperationspartnern festangestellt, beziehen ein Gehalt, entrichten im Heimatland Steuern sowie Beiträge für die Renten-, Arbeitslosen- und Krankenversicherung, sind also im vollen Umfang sozialversichert.</p>
    <div class="photo" role="img" aria-label="Foto: drei Senioren lächelnd im Garten" style="left:40px;top:380px;width:148px;height:100px;background:linear-gradient(135deg,#6b7a4e,#c98a7a 55%,#8fb0d8)"></div>
  </article>

  <article class="panel">
    <h2 class="heading">Kosten</h2>
    <h3 class="subhead">Betreuungskosten pro Monat für eine Betreuungskraft:</h3>
    <table class="cost-table">
      <tr><td>Geringe Kenntnisse:</td><td>1876,- €</td></tr>
      <tr><td>Ausreichende Kenntnisse:</td><td>1976,- €</td></tr>
      <tr><td>Mittlere Kenntnisse:</td><td>2076,- €</td></tr>
      <tr><td>Gute Kenntnisse:</td><td>2276,- €</td></tr>
      <tr><td>Sehr gute Kenntnisse:</td><td>2426,- €</td></tr>
      <tr><td>Schwere Pflegefälle/Betreuung einer 2. Person:</td><td>individuell</td></tr>
      <tr><td>An- und Abreise (beide Fahrten zusammen):</td><td>150 €</td></tr>
      <tr><td>Zusätzlich:</td><td>Kost &amp; Logis</td></tr>
    </table>
    <h2 class="heading" style="margin-top:12px">Kontakt</h2>
    <table class="contact">
      <tr><td>TELEFON:</td><td>0431 - 5507210*<br>*Mo. – Fr. 13.00 Uhr bis 15.00 Uhr und 14.00 Uhr bis 16.00 Uhr (Unsere Kunden können uns auch am Wochenende über eine zusätzliche Rufnummer erreichen.)</td></tr>
      <tr><td>FAX:</td><td>0431 - 5507219</td></tr>
      <tr><td>INTERNET:</td><td>www.curavita-pflegehilfe.de</td></tr>
      <tr><td>POST:</td><td>Curavita UG (haftungsbeschränkt)<br>Lindenweg 12<br>24103 Kiel, Deutschland</td></tr>
    </table>
    <p style="font-weight:700;margin-top:3px">Persönliche Termine nach Vereinbarung</p>
    <p>Wir freuen uns auf Ihre Anfrage.</p>
    <div role="img" aria-label="Foto: das Team vor hellem Hintergrund" style="position:absolute;left:16px;top:418px;width:84px;height:52px;background:linear-gradient(180deg,#e8e8e8,#3a3438)"></div>
    <p style="position:absolute;left:108px;top:418px;width:110px;font-size:5.6px">Curavita UG (haftungsbeschränkt)<br>Geschäftsführender Gesellschafter:<br>Jonas Weller<br>Handelsregister: HRB 20417 KI, Amtsgericht Kiel</p>
  </article>

  <article class="panel cover">
    <div class="brand brand--cover">Curavita</div>
    <div class="tagline">– Daheim gut umsorgt –</div>
    <div class="photo" role="img" aria-label="Foto: Pflegerin und ältere Dame Wange an Wange" style="left:20px;top:120px;width:150px;height:150px;border-color:#fff;background:radial-gradient(circle at 45% 45%,#f1d9c4,#c99a72 60%,#e9eef5)"></div>
    <div class="badge" style="left:128px;top:168px;width:112px;height:112px"><span class="brand">Curavita</span></div>
    <div class="photo" role="img" aria-label="Foto: Pfleger hilft Senior mit Rollator" style="left:58px;top:255px;width:112px;height:112px;border-color:#fff;background:linear-gradient(135deg,#f3f3f0,#c8c4bb 60%,#9db2cf)"></div>
    <div class="badge" style="left:164px;top:336px;width:50px;height:50px"><span class="brand" style="font-size:7px">Curavita</span></div>
    <div class="badge" style="left:10px;top:364px;width:76px;height:76px"><span class="brand" style="font-size:9px">Curavita</span></div>
  </article>
</section>

<section class="spread spread--inside">
  <article class="panel">
    <h2 class="heading" style="font-size:11px">Situation</h2>
    <h3 class="subhead">Sie haben einen Angehörigen, der Betreuung benötigt?</h3>
    <p>Die notwendige Unterstützung überschreitet Ihre zeitlichen oder auch physischen und psychischen Möglichkeiten?</p>
    <p>Ihnen liegt viel daran, dass Ihr Angehöriger liebevolle Betreuung erhält?</p>
    <p>Sie möchten nicht, dass Ihr Angehöriger seinen Lebensabend in einem Heim verbringen muss?</p>
    <p>Wir möchten und können Ihnen hier weiterhelfen.</p>
    <p>Wir vermitteln Ihnen liebevolle osteuropäische Betreuungskräfte, die im Haushalt Ihres Angehörigen leben und ihn im Alltag begleiten.</p>
    <p>Auch wenn die osteuropäische Betreuerin bei Ihnen ist, stehen wir Ihnen weiterhin mit Rat und Tat zur Verfügung.</p>
    <p>Die Betreuungskraft sollte bei Ihrem Angehörigen so lange bleiben, wie er die Betreuung benötigt.</p>
    <p>Gern arbeiten wir auch mit örtlichen ambulanten Pflegediensten zusammen, die medizinische Maßnahmen übernehmen.</p>
    <div class="brand brand--inline">Curavita</div>
    <div class="tagline--inline">– Daheim gut umsorgt –</div>
    <div class="photo" role="img" aria-label="Foto: junge Frau umarmt lachende Seniorin" style="left:44px;top:362px;width:140px;height:112px;background:linear-gradient(135deg,#b07a52,#e6c6ad 55%,#8a7a6c)"></div>
  </article>

  <article class="panel">
    <h2 class="heading">Philosophie</h2>
    <h3 class="subhead">„Einen alten Baum verpflanzt man nicht“</h3>
    <p>In aller Regel fühlt sich eine pflegebedürftige Person in ihrer angestammten Umgebung am wohlsten.</p>
    <p>Sie befinden sich zurzeit vermutlich an einem Punkt, an dem Sie prüfen, wie die Pflege und Betreuung eines nahen Angehörigen zu organisieren ist und stellen sich die Frage, ob Ihr Angehöriger zu Hause bleiben kann.</p>
    <p>Ein Seniorenheim ist oftmals die einfachste Lösung – für die Angehörigen. Entspricht diese Lösung aber auch dem Wunsch der betreffenden Person? Das Pflegepersonal in Heimen ist meist sehr eingespannt, die Zeit für persönliche Zuwendung ist daher häufig knapp bemessen.</p>
    <p>Wir sagen nicht, dass die von uns vermittelten Betreuungskräfte grundsätzlich und immer die bessere Lösung sind, aber die Wahrscheinlichkeit, dass es der zu betreuenden Person zu Hause gut geht, ist deutlich erhöht.</p>
    <h2 class="heading" style="margin-top:10px">Konzept</h2>
    <div class="numhead">1. 24 Stunden Pflege</div>
    <p>Die osteuropäische Betreuerin wohnt bei der zu betreuenden Person und kann sich so jederzeit um diese kümmern. Sie führt den Haushalt, übernimmt Hilfestellungen bei der Grundpflege und begleitet bei Spaziergängen.</p>
    <div class="numhead">2. Rahmenbedingungen</div>
    <p>Die Betreuungskraft benötigt ein eigenes Zimmer. Die Mitbenutzung von Bad und Küche muss möglich sein. Kost und Logis sind frei.</p>
  </article>

  <article class="panel">
    <div class="numhead" style="margin-top:0">3. Arbeitszeit bei der 24 Stunden Seniorenpflege</div>
    <p>Die Anwesenheit beträgt 24 Stunden. Aber natürlich benötigt die Betreuungskraft auch Freizeit, sie kann nicht Tag und Nacht arbeiten.</p>
    <div class="numhead">4. Einsatzdauer</div>
    <p>Die Betreuerinnen haben ihre Heimat in Polen und Tschechien. Sie bleiben in der Regel 8 bis 12 Wochen, danach übernimmt eine Kollegin. Ein fester Wechsel zwischen zwei Betreuungskräften hat sich bewährt.</p>
    <div class="numhead">5. Deutschkenntnisse</div>
    <p>Hier bieten wir 5 Abstufungen an:</p>
    <div class="list-grid">
      <span>Geringe Kenntnisse:</span><span>Verstehen / Sprechen wenig</span>
      <span>Ausreichende Kenntnisse:</span><span>Einfache Gespräche</span>
      <span>Mittlere Kenntnisse:</span><span>Vieles wird verstanden</span>
      <span>Gute Kenntnisse:</span><span>Detaillierte Gespräche</span>
      <span>Sehr gute Kenntnisse:</span><span>Ohne Einschränkungen</span>
    </div>
    <div class="numhead">6. Rechnungen</div>
    <p>Jeweils zum Monatsende erhalten Sie eine Rechnung. Der Rechnungsausgleich erfolgt per Überweisung.</p>
    <div class="numhead">7. Kündigungsfristen</div>
    <p>Die Verträge können ohne Angabe von Gründen mit einer Frist von 7 Tagen gekündigt werden.</p>
  </article>
</section>

</body>
</html>
```